Tumble Tail (Pet Supplies) Home Page

For our Tumble Tail website, we want this to be fun and playful but with a touch of your creativity! Tumble Tail is a fun-loving brand that sells pet supplies and accessories focused on accentuating the love between pets and their owners. We want to advertise these products in a welcoming way, making the customer receive the happiness the brand offers.

Target Market(s)

Main demo: Female pet owners online shopping 18-34. Secondary demo: All pet owners online shopping 18-34.

Number of Pages Required

1 page

```html
<!DOCTYPE html>
<html lang="en">
<head>
<meta charset="utf-8">
<title>Tumble Tail – Pet Supplies</title>
<link href="https://fonts.googleapis.com/css2?family=Montserrat:ital,wght@0,400;0,500;0,600;0,700;0,800;0,900;1,400;1,500&family=Sniglet:wght@400;800&family=Pacifico&display=swap" rel="stylesheet">
<style>
:root{
  --teal:#26c6cb;
  --purple:#9447a9;
  --orange:#fc8a3d;
  --star:#f7a21b;
  --ink:#222;
  --white:#fff;
  --fun:'Sniglet',sans-serif;
}
*{box-sizing:border-box;margin:0;padding:0}
html,body{width:1200px;height:3382px;overflow:hidden}
body{position:relative;font-family:'Montserrat',sans-serif;color:var(--ink);background:var(--white)}
.abs{position:absolute}

/* top bar + header */
.topbar{left:0;top:0;width:1200px;height:29px;background:var(--purple);color:var(--white);font-size:12px}
.topbar .social{left:134px;top:9px;display:flex;gap:8px}
.topbar .social span{width:10px;height:10px;border-radius:50%;background:var(--white);display:block}
.topbar .account{right:137px;top:7px;font-weight:500}
.header{left:0;top:29px;width:1200px;height:94px;background:var(--teal)}
.brand{left:130px;top:40px;color:var(--white);font-family:var(--fun);font-weight:800;font-size:18px;display:flex;flex-direction:column;align-items:center;white-space:nowrap}
.brand .mark{width:34px;height:34px;border:4px solid var(--white);border-radius:50%;margin-bottom:6px}
.nav{right:136px;top:84px;display:flex;gap:26px;align-items:center;color:var(--white);font-size:14px;font-weight:500;white-space:nowrap}
.nav svg{display:block}

/* hero */
.hero{left:0;top:123px;width:1200px;height:553px;background:linear-gradient(110deg,#3a2a1d 0%,#6b5038 30%,#c99a72 55%,#a38769 75%,#5a4a40 100%)}
.hero-copy{right:138px;top:434px;text-align:right;color:var(--white);font-weight:600;font-size:22px;line-height:29px;letter-spacing:-.2px;white-space:nowrap}
.btn-shop{left:903px;top:533px;width:159px;height:38px;border-radius:19px;background:var(--orange);color:var(--white);font-size:17px;font-weight:600;display:flex;align-items:center;justify-content:center}
.hero-arrow{top:390px;width:20px;height:20px;border-left:2px solid rgba(255,255,255,.5);border-bottom:2px solid rgba(255,255,255,.5)}

/* promo */
.promo{left:0;top:676px;width:1200px;height:109px;background:var(--purple);overflow:hidden}
.promo .dot{position:absolute;border-radius:50%}
.promo-title{left:0;width:1200px;top:12px;text-align:center;font-family:'Pacifico',cursive;color:var(--white);font-size:30px;white-space:nowrap}
.promo-sub{left:0;width:1200px;top:58px;text-align:center;font-family:'Pacifico',cursive;color:var(--orange);font-size:21px;white-space:nowrap}
.promo-pup{left:880px;top:18px;width:160px;height:90px;border-radius:50% 50% 8px 8px;background:linear-gradient(180deg,#f3dcb0,#d9b27b)}

/* section heads */
.section-title{left:0;width:1200px;text-align:center;font-family:var(--fun);font-weight:800;color:var(--purple);font-size:32px;letter-spacing:1px}

/* products */
.product{width:203px}
.product .photo{height:243px;border:2px solid var(--teal);background:linear-gradient(160deg,#f6f6f6,#d5d5d5 55%,#b9b9b9);display:block}
.product .name{margin-top:14px;text-align:center;font-weight:600;font-size:15px;white-space:nowrap}
.product .stars{margin-top:9px;text-align:center;color:var(--star);font-size:21px;letter-spacing:-1px;line-height:1}
.product .price{margin-top:9px;text-align:center;font-size:15px}
.product .cart{margin-top:10px;height:36px;background:var(--teal);color:var(--white);font-size:15px;font-weight:500;display:flex;align-items:center;justify-content:center}

/* buy now band */
.bnpl{left:0;top:1880px;width:1200px;height:170px;background:var(--teal)}
.bnpl-badge{left:288px;top:1893px;width:290px;height:138px}
.bnpl-badge .txt{position:absolute;left:26px;top:26px;color:var(--white);font-weight:900;transform:rotate(-4deg);line-height:1;white-space:nowrap}
.bnpl-badge .big{font-size:48px;letter-spacing:1px}
.bnpl-badge .small{font-size:30px;margin:2px 0 0 36px}
.partner{top:1944px;color:var(--white);font-weight:600;font-size:30px;display:flex;align-items:center;gap:10px;white-space:nowrap;line-height:36px}
.partner .sq{width:30px;height:30px;border-radius:50%;background:var(--white)}
.divider{left:797px;top:1935px;width:2px;height:62px;background:rgba(255,255,255,.85)}

/* testimonials */
.bubble{border-radius:26px;color:var(--white);font-style:italic;font-size:20px;line-height:28px;padding:0 40px;display:flex;align-items:center}
.bubble.teal{background:var(--teal)}
.bubble.orange{background:var(--orange)}
.bubble.purple{background:var(--purple)}
.blob{position:absolute;border-radius:50%}
.avatar{border-radius:50%;border:4px solid var(--white)}
.pet-tag{height:26px;border-radius:13px;color:var(--white);font-family:var(--fun);font-size:16px;display:flex;align-items:center;justify-content:center;white-space:nowrap}

/* floating */
.rewards{left:30px;top:3104px;width:112px;height:42px;border-radius:21px;background:#3e3a8c;color:var(--white);font-size:12px;display:flex;align-items:center;justify-content:center;gap:6px;box-shadow:0 3px 8px rgba(0,0,0,.25)}
.rewards i{width:14px;height:14px;background:#b6b4f0;border-radius:3px;display:block}
.chat{left:1116px;top:3100px;width:48px;height:48px;border-radius:50%;background:#c8def5;box-shadow:0 3px 8px rgba(0,0,0,.2);display:flex;align-items:center;justify-content:center}

/* footer */
.footer{left:0;top:3178px;width:1200px;height:178px;background:var(--teal);color:var(--white)}
.footer-brand{left:130px;top:3206px;width:156px;display:flex;flex-direction:column;align-items:center;color:var(--white);font-family:var(--fun);font-weight:800;font-size:28px;white-space:nowrap}
.footer-brand .mark{width:56px;height:56px;border:6px solid var(--white);border-radius:50%;margin-bottom:14px}
.fcol{top:3196px;color:var(--white);font-size:11px;line-height:23.5px;white-space:nowrap}
.fcol h4{font-family:var(--fun);font-weight:800;font-size:15px;letter-spacing:.5px;margin-bottom:4px}
.fcol .ico{display:inline-block;width:9px;height:9px;border:1.5px solid var(--white);border-radius:2px;margin-right:5px;vertical-align:-1px}
.fsocial{display:flex;gap:8px;margin-top:6px}
.fsocial span{width:22px;height:22px;border:1.5px solid var(--white);border-radius:50%;display:block}
.field{width:178px;height:25px;border:1.5px solid var(--white);border-radius:13px;font-size:10px;text-align:right;padding:5px 12px 0 0;margin-top:10px}
.subscribe{margin:10px 0 0 94px;width:84px;height:25px;border-radius:13px;background:var(--white);color:var(--ink);font-size:10px;font-weight:600;display:flex;align-items:center;justify-content:center}
.copyright{left:0;top:3356px;width:1200px;height:26px;background:var(--purple);color:var(--white);font-size:11px;display:flex;align-items:center;justify-content:center}
</style>
</head>
<body>

<div class="abs topbar">
  <div class="abs social"><span></span><span></span><span></span></div>
  <div class="abs account">My Account</div>
</div>

<header class="abs header"></header>
<div class="abs brand"><span class="mark"></span>Tumble Tail</div>
<nav class="abs nav">
  <span>Home</span><span>Shop</span><span>Our Story</span><span>Boop Blog</span><span>Pet History 101</span>
  <svg width="16" height="16" viewBox="0 0 16 16" fill="#fff"><path d="M1 2h2.5l2 8h7l2-6H5" stroke="#fff" stroke-width="1.6" fill="none"/><circle cx="6.5" cy="13.5" r="1.4"/><circle cx="12" cy="13.5" r="1.4"/></svg>
  <svg width="14" height="14" viewBox="0 0 14 14"><circle cx="6" cy="6" r="4.5" stroke="#fff" stroke-width="1.6" fill="none"/><path d="M9.5 9.5 13 13" stroke="#fff" stroke-width="1.6"/></svg>
</nav>

<section class="abs hero" role="img" aria-label="Photo of a smiling woman hugging a happy tri-colour dog outdoors"></section>
<div class="abs hero-arrow" style="left:80px;transform:rotate(45deg)"></div>
<div class="abs hero-arrow" style="left:1100px;transform:rotate(-135deg)"></div>
<div class="abs hero-copy">LOREM IPSUM DOLOR SIT AMET<br>CONSECTETUR ADIPISCING SED<br>DO EIUSMOD TEMPOR INCI</div>
<div class="abs btn-shop">Shop Now</div>

<section class="abs promo">
  <span class="dot" style="left:290px;top:-56px;width:116px;height:116px;background:var(--orange)"></span>
  <span class="dot" style="left:136px;top:58px;width:134px;height:134px;background:var(--teal)"></span>
  <span class="dot" style="left:1040px;top:-32px;width:64px;height:64px;background:var(--white)"></span>
  <span class="dot" style="left:865px;top:10px;width:160px;height:160px;background:#a766ba"></span>
  <div class="abs promo-pup" role="img" aria-label="Photo of a golden retriever puppy lying down"></div>
  <div class="abs promo-title">50% off sale going on now!</div>
  <div class="abs promo-sub">Because we love you too</div>
</section>

<h2 class="abs section-title" style="top:857px">Furry Favorites</h2>

<div class="abs product" style="left:144px;top:945px"><div class="photo" role="img" aria-label="Grey dog travel bag with bowls and accessories"></div><div class="name">Top Dog Travel Bag</div><div class="stars">★★★★★</div><div class="price">$55.00</div><div class="cart">Add to Cart</div></div>
<div class="abs product" style="left:381px;top:945px"><div class="photo" role="img" aria-label="Grey dog travel bag with bowls and accessories"></div><div class="name">Top Dog Travel Bag</div><div class="stars">★★★★★</div><div class="price">$55.00</div><div class="cart">Add to Cart</div></div>
<div class="abs product" style="left:618px;top:945px"><div class="photo" role="img" aria-label="Grey dog travel bag with bowls and accessories"></div><div class="name">Top Dog Travel Bag</div><div class="stars">★★★★★</div><div class="price">$55.00</div><div class="cart">Add to Cart</div></div>
<div class="abs product" style="left:855px;top:945px"><div class="photo" role="img" aria-label="Grey dog travel bag with bowls and accessories"></div><div class="name">Top Dog Travel Bag</div><div class="stars">★★★★★</div><div class="price">$55.00</div><div class="cart">Add to Cart</div></div>

<div class="abs product" style="left:144px;top:1383px"><div class="photo" role="img" aria-label="Grey dog travel bag with bowls and accessories"></div><div class="name">Top Dog Travel Bag</div><div class="stars">★★★★★</div><div class="price">$55.00</div><div class="cart">Add to Cart</div></div>
<div class="abs product" style="left:381px;top:1383px"><div class="photo" role="img" aria-label="Grey dog travel bag with bowls and accessories"></div><div class="name">Top Dog Travel Bag</div><div class="stars">★★★★★</div><div class="price">$55.00</div><div class="cart">Add to Cart</div></div>
<div class="abs product" style="left:618px;top:1383px"><div class="photo" role="img" aria-label="Grey dog travel bag with bowls and accessories"></div><div class="name">Top Dog Travel Bag</div><div class="stars">★★★★★</div><div class="price">$55.00</div><div class="cart">Add to Cart</div></div>
<div class="abs product" style="left:855px;top:1383px"><div class="photo" role="img" aria-label="Grey dog travel bag with bowls and accessories"></div><div class="name">Top Dog Travel Bag</div><div class="stars">★★★★★</div><div class="price">$55.00</div><div class="cart">Add to Cart</div></div>

<section class="abs bnpl"></section>
<div class="abs bnpl-badge">
  <svg width="290" height="138" viewBox="0 0 290 138">
    <polygon points="40,10 280,22 276,36 40,36" fill="#fff"/>
    <polygon points="0,26 290,10 290,110 2,126" fill="#9447a9"/>
    <polygon points="70,118 270,108 266,138 70,134" fill="#fff"/>
  </svg>
  <div class="txt"><div class="big">BUY NOW</div><div class="small">PAY LATER</div></div>
</div>
<div class="abs partner" style="left:630px"><span class="sq"></span>Crumbly</div>
<div class="abs divider"></div>
<div class="abs partner" style="left:814px">Paywise</div>

<h2 class="abs section-title" style="top:2120px">Testimonials</h2>

<!-- testimonial 1 -->
<span class="blob" style="left:128px;top:2192px;width:196px;height:160px;background:var(--teal);border-radius:48%"></span>
<span class="blob" style="left:235px;top:2170px;width:50px;height:50px;background:var(--teal)"></span>
<span class="blob" style="left:160px;top:2350px;width:30px;height:30px;background:var(--teal)"></span>
<span class="blob" style="left:204px;top:2376px;width:16px;height:16px;background:var(--teal)"></span>
<div class="abs avatar" style="left:147px;top:2193px;width:152px;height:152px;background:linear-gradient(160deg,#f2e3c9,#c99f63)" role="img" aria-label="Photo of Bella, a golden puppy"></div>
<div class="abs pet-tag" style="left:200px;top:2341px;width:118px;background:var(--teal)">Bella (dog)</div>
<span class="blob" style="left:836px;top:2190px;width:48px;height:48px;background:var(--teal)"></span>
<span class="blob" style="left:948px;top:2310px;width:60px;height:60px;background:var(--teal)"></span>
<span class="blob" style="left:1050px;top:2296px;width:14px;height:14px;background:var(--teal)"></span>
<span class="blob" style="left:391px;top:2188px;width:10px;height:10px;background:var(--teal)"></span>
<span class="blob" style="left:895px;top:2186px;width:12px;height:12px;background:var(--teal)"></span>
<div class="abs bubble teal" style="left:337px;top:2208px;width:716px;height:124px">“Before Tumble Tail my human bought me gifts that made me want to dig a hole under the fence and run. Now I still dig, but it’s to bury all my awesome toys!”</div>

<!-- testimonial 2 -->
<span class="blob" style="left:880px;top:2400px;width:178px;height:178px;background:var(--orange)"></span>
<span class="blob" style="left:990px;top:2578px;width:30px;height:30px;background:var(--orange)"></span>
<span class="blob" style="left:964px;top:2604px;width:16px;height:16px;background:var(--orange)"></span>
<div class="abs avatar" style="left:887px;top:2414px;width:150px;height:150px;background:linear-gradient(160deg,#f7c28a,#d97a2f)" role="img" aria-label="Photo of Leo, a ginger kitten"></div>
<div class="abs pet-tag" style="left:870px;top:2562px;width:94px;background:var(--orange)">Leo (cat)</div>
<span class="blob" style="left:120px;top:2436px;width:40px;height:40px;background:var(--orange)"></span>
<span class="blob" style="left:540px;top:2412px;width:46px;height:46px;background:var(--orange)"></span>
<span class="blob" style="left:745px;top:2540px;width:48px;height:48px;background:var(--orange)"></span>
<span class="blob" style="left:698px;top:2412px;width:12px;height:12px;background:var(--orange)"></span>
<div class="abs bubble orange" style="left:139px;top:2432px;width:717px;height:123px">“My favorite thing to do is watch the birds out the window. Those birds are lucky my house is full of comfy stuff from Tumble Tail so I don’t ever want to leave.”</div>

<!-- testimonial 3 -->
<span class="blob" style="left:128px;top:2638px;width:196px;height:160px;background:var(--purple);border-radius:48%"></span>
<span class="blob" style="left:235px;top:2616px;width:50px;height:50px;background:var(--purple)"></span>
<span class="blob" style="left:160px;top:2796px;width:30px;height:30px;background:var(--purple)"></span>
<span class="blob" style="left:204px;top:2822px;width:16px;height:16px;background:var(--purple)"></span>
<div class="abs avatar" style="left:147px;top:2638px;width:152px;height:152px;background:linear-gradient(160deg,#cfe3a8,#d79b5a)" role="img" aria-label="Photo of Max, a fluffy happy dog"></div>
<div class="abs pet-tag" style="left:200px;top:2786px;width:118px;background:var(--purple)">Max (dog)</div>
<span class="blob" style="left:836px;top:2636px;width:48px;height:48px;background:var(--purple)"></span>
<span class="blob" style="left:948px;top:2756px;width:60px;height:60px;background:var(--purple)"></span>
<span class="blob" style="left:1050px;top:2742px;width:14px;height:14px;background:var(--purple)"></span>
<span class="blob" style="left:895px;top:2632px;width:12px;height:12px;background:var(--purple)"></span>
<div class="abs bubble purple" style="left:337px;top:2654px;width:716px;height:123px;align-items:flex-start;padding-top:26px">“Tumble Tail is the absolute best! Now if you’ll excuse me I think I heard someone drop some food on the floor.”</div>

<!-- testimonial 4 -->
<span class="blob" style="left:880px;top:2846px;width:178px;height:178px;background:var(--orange)"></span>
<span class="blob" style="left:990px;top:3022px;width:30px;height:30px;background:var(--orange)"></span>
<span class="blob" style="left:964px;top:3048px;width:16px;height:16px;background:var(--orange)"></span>
<div class="abs avatar" style="left:887px;top:2862px;width:150px;height:150px;background:linear-gradient(160deg,#3a5a2a,#e76a2a)" role="img" aria-label="Photo of Dora, an orange goldfish"></div>
<div class="abs pet-tag" style="left:870px;top:3006px;width:104px;background:var(--orange)">Dora (Fish)</div>
<span class="blob" style="left:118px;top:2880px;width:40px;height:40px;background:var(--orange)"></span>
<span class="blob" style="left:536px;top:2858px;width:46px;height:46px;background:var(--orange)"></span>
<span class="blob" style="left:742px;top:2984px;width:48px;height:48px;background:var(--orange)"></span>
<span class="blob" style="left:694px;top:2856px;width:12px;height:12px;background:var(--orange)"></span>
<div class="abs bubble orange" style="left:137px;top:2878px;width:716px;height:123px;align-items:flex-start;padding-top:26px">“I could rave about Tumble Tail until I was blue in the gills! Those other brands just seem a bit fishy to me.”</div>

<div class="abs rewards"><i></i>Rewards</div>
<div class="abs chat"><svg width="18" height="14" viewBox="0 0 18 14"><rect x="1" y="1" width="16" height="10" rx="3" fill="#3e6fb0"/><path d="M5 6h8" stroke="#fff" stroke-width="1.5"/></svg></div>

<footer class="abs footer"></footer>
<div class="abs footer-brand"><span class="mark"></span>Tumble Tail</div>
<div class="abs fcol" style="left:336px"><h4>COMPANY</h4>Home<br>Shop<br>Our Story<br>Boop Blog<br>Pet History 101</div>
<div class="abs fcol" style="left:478px"><h4>HELP &amp; SUPPORT</h4>Returns &amp; Exchanges<br>FAQ<br>help@tumbletail.com<br>Search</div>
<div class="abs fcol" style="left:679px"><h4>CONTACT</h4><span class="ico"></span>555-0142-0199<br><span class="ico"></span>help@tumbletail.com<div class="fsocial"><span></span><span></span><span></span></div></div>
<div class="abs fcol" style="left:887px"><h4>Sign up to our newsletter</h4><div class="field">Name</div><div class="field">Email</div><div class="subscribe">Subscribe</div></div>
<div class="abs copyright">Copyright 2021 tumbletail.com: All rights reserved</div>

</body>
</html>
```